Design a sharp Business Card, Stationary, and PowerPoint Template for Harbor Lantern Group (HLG)
Harbor Lantern Group (HLG) is a consulting firm with a mission
Professional
Maren Coleby Ashdown
Managing Director
4870 Larkspur Blvd. NW
Suite 2300
Washington, DC 20417
maren@harborlntn.example
www.harborlntn.example
I'm looking for something sharp that incorporates the colors of the logo.
Business card designs (only), please include this text:
We work with the military, private sector, and nonprofits to protect people affected by conflict and disaster.
This is the logo for Harbor Lantern Group (HLG). The black and red color combo is preferred.
For design purposes, the symbol can be used separately from the text and watermarked.

```html
<!DOCTYPE html>
<html lang="en">
<head>
<meta charset="utf-8">
<title>Harbor Lantern Group – Business Card</title>
<link href="https://fonts.googleapis.com/css2?family=Open+Sans:ital,wght@0,300;0,400;0,600;1,400;1,600&display=swap" rel="stylesheet">
<style>
  :root {
    --bg: #e9e6e1;
    --card: #ffffff;
    --ink: #2b2b2b;
    --ink-soft: #4a4a4a;
    --accent: #e1232b;
    --band-dark: #2f2f31;
  }
  * { margin: 0; padding: 0; box-sizing: border-box; }
  html, body {
    width: 1200px;
    height: 914px;
    overflow: hidden;
    background: var(--bg);
    font-family: "Open Sans", Arial, sans-serif;
    color: var(--ink);
  }
  .business-card {
    position: absolute;
    left: 100px;
    top: 171px;
    width: 1000px;
    height: 572px;
    background: var(--card);
    box-shadow: 0 10px 30px rgba(0,0,0,0.15);
    overflow: hidden;
  }
  .card-bands {
    position: absolute;
    left: 0; top: 0;
    width: 1000px; height: 572px;
  }
  .brand {
    position: absolute;
    left: 400px;
    top: 96px;
    display: flex;
    align-items: center;
    gap: 22px;
  }
  .brand-dot {
    width: 74px; height: 74px;
    border-radius: 50%;
    background: var(--accent);
  }
  .brand-name {
    font-weight: 300;
    font-size: 30px;
    line-height: 1.25;
    letter-spacing: 6px;
    text-transform: uppercase;
    color: var(--ink);
  }
  .holder {
    position: absolute;
    right: 520px;
    top: 262px;
    text-align: right;
    font-style: italic;
    font-size: 17px;
    line-height: 1.5;
    color: var(--ink-soft);
  }
  .holder-name {
    font-weight: 600;
    font-size: 20px;
    color: var(--accent);
  }
  .contact-list {
    position: absolute;
    left: 520px;
    top: 268px;
    list-style: none;
    font-size: 17px;
    line-height: 1;
    color: var(--ink-soft);
  }
  .contact-list li {
    display: flex;
    align-items: center;
    gap: 10px;
    height: 25px;
  }
  .contact-icon {
    width: 18px; height: 18px;
    flex: none;
  }
  .mission {
    position: absolute;
    left: 60px;
    top: 482px;
    width: 400px;
    font-style: italic;
    font-size: 14px;
    line-height: 1.5;
    color: var(--ink-soft);
  }
</style>
</head>
<body>
  <section class="business-card">
    <svg class="card-bands" viewBox="0 0 1000 572" aria-hidden="true">
      <polygon points="0,434 500,434 484,462 0,462" fill="var(--band-dark)"/>
      <polygon points="486,470 1000,470 1000,508 466,508" fill="var(--accent)"/>
    </svg>

    <div class="brand">
      <div class="brand-dot"></div>
      <div class="brand-name">Harbor<br>Lantern<br>Group</div>
    </div>

    <div class="holder">
      <p class="holder-name">Maren Coleby Ashdown</p>
      <p class="holder-title">Managing Director</p>
      <p>4870 Larkspur Blvd. NW</p>
      <p>Suite 2300 Washington, DC 20417</p>
    </div>

    <ul class="contact-list">
      <li>
        <svg class="contact-icon" viewBox="0 0 18 18"><circle cx="9" cy="9" r="9" fill="var(--accent)"/><path d="M6 4.5l2 2-1 1.2c.6 1.3 1.6 2.3 2.9 2.9l1.2-1 2 2-1.2 1.4C8.5 12.7 5.3 9.5 4.6 5.7z" fill="#fff"/></svg>
        <span>202-555-0148</span>
      </li>
      <li>
        <svg class="contact-icon" viewBox="0 0 18 18"><circle cx="9" cy="9" r="9" fill="var(--accent)"/><rect x="6" y="4" width="6" height="10" rx="1" fill="#fff"/><rect x="7" y="5.2" width="4" height="6.5" fill="var(--accent)"/></svg>
        <span>202-555-0193</span>
      </li>
      <li>
        <svg class="contact-icon" viewBox="0 0 18 18"><circle cx="9" cy="9" r="9" fill="var(--accent)"/><rect x="4.5" y="5.5" width="9" height="7" fill="#fff"/><path d="M4.5 5.5L9 9.5l4.5-4" fill="none" stroke="var(--accent)" stroke-width="1"/></svg>
        <span>maren@harborlntn.example</span>
      </li>
      <li>
        <svg class="contact-icon" viewBox="0 0 18 18"><circle cx="9" cy="9" r="9" fill="var(--accent)"/><circle cx="9" cy="9" r="4.5" fill="none" stroke="#fff" stroke-width="1.2"/><path d="M4.5 9h9M9 4.5c-2 2.5-2 6.5 0 9M9 4.5c2 2.5 2 6.5 0 9" fill="none" stroke="#fff" stroke-width="1"/></svg>
        <span>www.harborlntn.example</span>
      </li>
    </ul>

    <p class="mission">We work with the military, private sector, and nonprofits to protect people affected by conflict and disaster.</p>
  </section>
</body>
</html>
```